Silver Heron Construction Services

Create a business card for my business consulting company
Danielle Vesk, Founder and CEO
4816 Alder Brook Way, Ste 100
Denver, CO. 80451
303.782.4190 cell
dvesk@silverheronconst.example
www.silverheronconst.example

Target Market(s)

Private Equity and Construction Companies

Industry/Entity Type

Business / Sales Consulting

Contact Information for Business Card

Tag Line that says "Where The Road To Success Is Always Under Construction"

Requirements
Must have
• Logo on both sides of the card.
Nice to have
• Add tagline to the same side of the card as my name and contact info

```html
<!DOCTYPE html>
<html lang="en">
<head>
<meta charset="utf-8">
<title>Silver Heron Construction Services – Business Cards</title>
<link rel="stylesheet" href="https://fonts.googleapis.com/css2?family=Cabin:wght@400;600;700&display=swap">
<style>
  :root {
    --canvas: #d9d4cc;
    --card-white: #ffffff;
    --card-shade: #ececec;
    --ink: #0b0b0b;
    --ink-soft: #4a4a4a;
    --band-text: #ffffff;
  }
  * { box-sizing: border-box; margin: 0; padding: 0; }
  html, body { width: 1200px; height: 900px; overflow: hidden; }
  body {
    background: var(--canvas);
    font-family: "Cabin", "Gill Sans", sans-serif;
    position: relative;
  }
  .card {
    position: absolute;
    width: 560px;
    height: 320px;
    background: linear-gradient(135deg, var(--card-white) 0%, var(--card-white) 45%, var(--card-shade) 100%);
    box-shadow: 0 14px 30px rgba(0,0,0,0.28);
    overflow: hidden;
  }
  .card--front { left: 70px; top: 80px; }
  .card--back  { left: 570px; top: 500px; }
  .card__band { position: absolute; inset: 0; width: 100%; height: 100%; }
  .tagline {
    position: absolute;
    right: 30px;
    top: 222px;
    width: 200px;
    color: var(--band-text);
    font-weight: 700;
    font-size: 17px;
    line-height: 1.3;
    text-align: right;
  }
  .brand {
    position: absolute;
    display: flex;
    align-items: center;
    gap: 12px;
    color: var(--ink);
    font-weight: 700;
  }
  .brand__mark { width: 18px; height: 18px; background: var(--ink); flex: none; }
  .brand__name { text-transform: uppercase; line-height: 1.05; }
  .brand__name span { display: block; }
  .card--front .brand { left: 70px; top: 95px; }
  .card--front .brand__name { font-size: 28px; }
  .card--front .brand__name span + span { font-size: 13px; letter-spacing: 0.22em; margin-top: 6px; }
  .card--back .brand { right: 40px; top: 44px; }
  .card--back .brand__mark { width: 12px; height: 12px; }
  .card--back .brand__name { font-size: 19px; }
  .card--back .brand__name span + span { font-size: 9px; letter-spacing: 0.2em; margin-top: 4px; }
  .contact {
    position: absolute;
    left: 40px;
    top: 110px;
    color: var(--ink-soft);
    font-size: 13.5px;
    line-height: 1.35;
  }
  .contact__name { color: var(--ink); font-weight: 700; font-size: 19px; text-transform: uppercase; }
  .contact__role { font-size: 14.5px; margin-bottom: 10px; }
  .contact__address { margin-left: 18px; margin-bottom: 10px; }
  .contact__line { display: flex; align-items: center; gap: 8px; margin-left: 18px; }
  .contact__icon { width: 13px; height: 13px; flex: none; }
</style>
</head>
<body>

<section class="card card--front" aria-label="Business card front">
  <svg class="card__band" viewBox="0 0 560 320" preserveAspectRatio="none" aria-hidden="true">
    <path d="M0 320 V252 H318 Q340 252 340 230 V212 Q340 190 362 190 H560 V320 Z" fill="var(--ink)"/>
  </svg>
  <div class="brand">
    <div class="brand__mark"></div>
    <div class="brand__name"><span>Silver Heron</span><span>Construction Services</span></div>
  </div>
  <p class="tagline">The Road To Success Is Always Under Construction</p>
</section>

<section class="card card--back" aria-label="Business card back">
  <svg class="card__band" viewBox="0 0 560 320" preserveAspectRatio="none" aria-hidden="true">
    <path d="M0 320 V252 H318 Q340 252 340 230 V212 Q340 190 362 190 H560 V320 Z" fill="var(--ink)"/>
  </svg>
  <div class="brand">
    <div class="brand__mark"></div>
    <div class="brand__name"><span>Silver Heron</span><span>Construction Services</span></div>
  </div>
  <div class="contact">
    <p class="contact__name">Danielle Vesk</p>
    <p class="contact__role">Founder and CEO</p>
    <p class="contact__address">4816 Alder Brook Way, Ste 100<br>Denver, CO. 80451</p>
    <p class="contact__line">
      <svg class="contact__icon" viewBox="0 0 16 16" aria-hidden="true"><path d="M3 1 L6 1 L7 5 L5 6.5 Q6.5 9.5 9.5 11 L11 9 L15 10 L15 13 Q15 15 13 15 Q1 14 1 3 Q1 1 3 1 Z" fill="var(--ink)"/></svg>
      303.782.4190
    </p>
    <p class="contact__line">
      <svg class="contact__icon" viewBox="0 0 16 16" aria-hidden="true"><rect x="1" y="3" width="14" height="10" fill="var(--ink)"/><path d="M1.5 3.5 L8 9 L14.5 3.5" fill="none" stroke="#fff" stroke-width="1.2"/></svg>
      dvesk@silverheronconst.example
    </p>
  </div>
  <p class="tagline">The Road To Success Is Always Under Construction</p>
</section>

</body>
</html>
```